Design packaging for our 'Cindral Wisp' personal massager (vibrator)!

Design our product box, please.

We will be selling a vibrator (personal massager on the website:-) ) in 4 different colours - please see attached. The box will be matt black, and we would love classy and understated, definitely not garish or raunchy. Note that the Barcode has to be on a white background, so we suspect we will need to stick that onto the box somewhere - probably the bottom, unless anyone has a better (more aesthetically pleasing) idea! Dimensions of the barcode must be between 1 inch x 2 inches and 2 inches x 3 inches(1 inch x 3 inches, or 2 inches by 2 inches, for eg) - if you can propose a spot, that would be great. The product has a pink satin travel pouch in the box, and product comes in pink, purple, Rose and Black. The box needs to stand out in photography, and the product will be sold online. Could add 'Heated Massager' somewhere, and colour of the product, too. Certifications that would be good to have on the box: CE and ROHS. There is a small insert box for the charger wire - would want 'Charger Wire' in matching script on this box. Script to match product name, please.

We included a potential logo for the box, and also our company logo. We are open to suggestions on the logo for the box, but the product name is Cindral Wisp (spelling intentionally different from Co. name), and it should tie in with our company logo in some way.

We will be super quick in obtaining any additional information required from the supplier, or answering any questions.

Target Market(s)

Audience: Mostly women (of all ages, hopefully)! Realistically, they'll be between the ages of 18 and 40 for the most part. They will be American (that's where our market is, but we anticipate moving to UK, Australia and Europe. Middle to high income earners. We expect they will be looking for subtlety and quality.

Font styles to use
Other font styles liked:
• See Product name logo attachment

Colors

Designer to choose colors to be used in the design.

Requirements
Must have
• Convey quality, understatement and link to our company logo in some way. Should stand out when photographed, and compared to competitors on online forum!
Should not have
• Crass, raunchy feel. No pictures of vibrators.

```html
<!DOCTYPE html>
<html lang="en">
<head>
<meta charset="utf-8">
<title>Cindral Wisp – Box Dielines</title>
<link href="https://fonts.googleapis.com/css2?family=Oswald:wght@400;500;600&display=swap" rel="stylesheet">
<style>
  :root {
    --paper: #ffffff;
    --board: #333333;
    --ink: #111111;
    --rose-top: #f5003a;
    --rose-bottom: #e6005c;
    --rose-accent: #e0002b;
    --rose-muted: #b8002c;
    --rose-band-text: #a8001f;
    --black-top: #1a0205;
    --black-mid: #000000;
    --black-bottom: #07031a;
    --brand-purple: #7b45ad;
    --icon-grey: #c9c9c9;
  }
  html, body {
    margin: 0;
    padding: 0;
    width: 1200px;
    height: 952px;
    overflow: hidden;
    background: var(--paper);
    font-family: "Oswald", sans-serif;
  }
  .sheet { position: relative; width: 1200px; height: 952px; }
  .variant-label {
    position: absolute;
    margin: 0;
    font-weight: 400;
    font-size: 20px;
    line-height: 24px;
    letter-spacing: 4px;
    color: var(--ink);
  }
  .dieline { position: absolute; width: 402px; height: 715px; }
  .dieline > svg { position: absolute; left: 0; top: 0; }

  .brand {
    position: absolute; left: 124px; width: 152px; top: 144px;
    display: flex; flex-direction: column; align-items: center; gap: 10px;
  }
  .brand-dot { display: block; width: 22px; height: 22px; border-radius: 50%; background: var(--brand-purple); }
  .brand-name {
    display: block; font-weight: 500; font-size: 16px; line-height: 20px; letter-spacing: 0.3px;
    color: var(--brand-purple); white-space: nowrap;
  }

  .product-name {
    position: absolute; left: 140px; top: 236px; width: 136px; margin: 0;
    font-weight: 600; font-size: 78px; line-height: 94px; letter-spacing: -1px;
  }
  .product-name .syllable {
    display: block; height: 94px;
    background: linear-gradient(100deg, #000 0%, #2a2a2a 45%, #000 60%, #3a3a3a 100%);
    -webkit-background-clip: text; background-clip: text; color: transparent;
  }
  .product-name .word {
    display: block; height: 60px; margin-top: -10px;
    font-weight: 500; font-size: 56px; line-height: 60px; letter-spacing: 0;
  }

  .tagline-band {
    position: absolute; left: 124px; width: 152px; top: 573px; height: 25px;
    display: flex; align-items: center; justify-content: center;
    font-size: 11.5px; letter-spacing: 2px; font-weight: 500; white-space: nowrap;
  }

  .feature {
    position: absolute; left: 278px; width: 80px;
    display: flex; flex-direction: column; align-items: center; gap: 11px;
  }
  .feature-icon { display: block; }
  .feature-label {
    display: block; font-size: 8.5px; letter-spacing: 1.5px; line-height: 10px;
    text-align: center; font-weight: 500;
  }

  .rose .product-name .word { color: var(--rose-accent); }
  .rose .tagline-band { background: var(--rose-accent); color: var(--rose-band-text); }
  .rose .feature { color: var(--rose-muted); }
  .black .product-name .word { color: #080808; }
  .black .tagline-band { background: #0a0a0a; color: #e8e8e8; }
  .black .feature { color: var(--icon-grey); }
</style>
</head>
<body>
<main class="sheet">

  <h2 class="variant-label" style="left:113px; top:107px;">ROSE</h2>
  <section class="dieline rose" style="left:114px; top:145px;">
    <svg width="402" height="715" viewBox="0 0 402 715">
      <defs>
        <linearGradient id="roseFill" x1="0" y1="0" x2="0.3" y2="1">
          <stop offset="0" stop-color="#f5003a"/>
          <stop offset="1" stop-color="#e6005c"/>
        </linearGradient>
      </defs>
      <g fill="url(#roseFill)">
        <path d="M17 87 H116 L121 118 H17 Z"/>
        <path d="M0 118 H121 V597 H0 V590 H17 V125 H0 Z"/>
        <rect x="0" y="125" width="17" height="465"/>
        <path d="M17 597 H121 L116 628 H17 Z"/>
        <path d="M284 87 H384 V118 H279 Z"/>
        <rect x="279" y="118" width="123" height="479"/>
        <path d="M279 597 H384 V628 H284 Z"/>
      </g>
      <rect x="124" y="0" width="152" height="715" rx="3" fill="#333333"/>
      <rect x="44" y="116" width="334" height="482" fill="none" stroke="#ffffff" stroke-opacity="0.18" stroke-width="0.8"/>
    </svg>
    <div class="brand"><span class="brand-dot"></span><span class="brand-name">Marlowe Direct LLC</span></div>
    <h1 class="product-name">
      <span class="syllable">CIN</span><span class="syllable">DRA</span><span class="syllable">L</span><span class="word">WISP</span>
    </h1>
    <div class="tagline-band">HEATED MASSAGER</div>
    <div class="feature" style="top:199px;">
      <svg class="feature-icon" width="44" height="44" viewBox="0 0 44 44"><g fill="none" stroke="currentColor"><circle cx="22" cy="22" r="20.5" stroke-width="2"/><path d="M20 10 h4 v15 a5 5 0 1 1 -4 0 z" stroke-width="1.6"/></g><circle cx="22" cy="29" r="2.5" fill="currentColor"/></svg>
      <span class="feature-label">HEATED<br>MASSAGER</span>
    </div>
    <div class="feature" style="top:327px;">
      <svg class="feature-icon" width="44" height="44" viewBox="0 0 44 44"><g fill="none" stroke="currentColor"><circle cx="22" cy="22" r="20.5" stroke-width="2"/><g stroke-width="1.7" stroke-linecap="round"><path d="M19 17 l8 8 a5 5 0 0 1 -8 0 a5 5 0 0 1 0 -8z"/><path d="M23 17 l4 -4 M27 21 l4 -4 M19 25 l-6 6"/></g></g></svg>
      <span class="feature-label">CHARGER<br>WIRE</span>
    </div>
    <div class="feature" style="top:456px;">
      <svg class="feature-icon" width="44" height="44" viewBox="0 0 44 44"><circle cx="22" cy="22" r="20.5" fill="none" stroke="currentColor" stroke-width="2"/><text x="22" y="25.5" text-anchor="middle" font-family="Oswald, sans-serif" font-size="9" font-weight="500" letter-spacing="1" fill="currentColor">ICON</text></svg>
      <span class="feature-label">TEXT</span>
    </div>
  </section>

  <h2 class="variant-label" style="left:686px; top:104px;">BLACK</h2>
  <section class="dieline black" style="left:687px; top:148px;">
    <svg width="402" height="715" viewBox="0 0 402 715">
      <defs>
        <linearGradient id="blackFill" x1="0" y1="0" x2="0.2" y2="1">
          <stop offset="0" stop-color="#1a0205"/>
          <stop offset="0.55" stop-color="#000000"/>
          <stop offset="1" stop-color="#07031a"/>
        </linearGradient>
      </defs>
      <g fill="url(#blackFill)">
        <path d="M17 87 H116 L121 118 H17 Z"/>
        <rect x="0" y="118" width="121" height="479"/>
        <path d="M17 597 H121 L116 628 H17 Z"/>
        <path d="M284 87 H384 V118 H279 Z"/>
        <rect x="279" y="118" width="123" height="479"/>
        <path d="M279 597 H384 V628 H284 Z"/>
      </g>
      <rect x="124" y="0" width="152" height="715" rx="3" fill="#333333"/>
      <rect x="44" y="116" width="334" height="482" fill="none" stroke="#ffffff" stroke-opacity="0.15" stroke-width="0.8"/>
    </svg>
    <div class="brand"><span class="brand-dot"></span><span class="brand-name">Marlowe Direct LLC</span></div>
    <h1 class="product-name">
      <span class="syllable">CIN</span><span class="syllable">DRA</span><span class="syllable">L</span><span class="word">WISP</span>
    </h1>
    <div class="tagline-band">HEATED MASSAGER</div>
    <div class="feature" style="top:199px;">
      <svg class="feature-icon" width="44" height="44" viewBox="0 0 44 44"><g fill="none" stroke="currentColor"><circle cx="22" cy="22" r="20.5" stroke-width="2"/><path d="M20 10 h4 v15 a5 5 0 1 1 -4 0 z" stroke-width="1.6"/></g><circle cx="22" cy="29" r="2.5" fill="currentColor"/></svg>
      <span class="feature-label">HEATED<br>MASSAGER</span>
    </div>
    <div class="feature" style="top:327px;">
      <svg class="feature-icon" width="44" height="44" viewBox="0 0 44 44"><g fill="none" stroke="currentColor"><circle cx="22" cy="22" r="20.5" stroke-width="2"/><g stroke-width="1.7" stroke-linecap="round"><path d="M19 17 l8 8 a5 5 0 0 1 -8 0 a5 5 0 0 1 0 -8z"/><path d="M23 17 l4 -4 M27 21 l4 -4 M19 25 l-6 6"/></g></g></svg>
      <span class="feature-label">CHARGER<br>WIRE</span>
    </div>
    <div class="feature" style="top:456px;">
      <svg class="feature-icon" width="44" height="44" viewBox="0 0 44 44"><circle cx="22" cy="22" r="20.5" fill="none" stroke="currentColor" stroke-width="2"/><text x="22" y="25.5" text-anchor="middle" font-family="Oswald, sans-serif" font-size="9" font-weight="500" letter-spacing="1" fill="currentColor">ICON</text></svg>
      <span class="feature-label">TEXT</span>
    </div>
  </section>

</main>
</body>
</html>
```